Powerpoint template for Trivia Company

Revamp of our current powerpoint template to make it more professional and fun for the players. Something worthy of a trivia company. Please see logo attached for potential colour - but also open to other ideas.

NO BRANDING REQUIRED (IE: No mention of our company or logo on the template please)

Target Market(s)

Bars/restaurants

Colors
3176b5
00a990

```html
<!DOCTYPE html>
<html lang="en">
<head>
<meta charset="utf-8">
<title>General Knowledge</title>
<link href="https://fonts.googleapis.com/css2?family=Archivo:wght@700;800&display=swap" rel="stylesheet">
<style>
  :root {
    --orange: #f2760e;
    --yellow: #ffe500;
    --teal: #27b3c6;
    --navy: #1c2a66;
  }
  html, body {
    margin: 0;
    padding: 0;
    overflow: hidden;
  }
  .slide {
    position: relative;
    width: 1200px;
    height: 675px;
    overflow: hidden;
    background-color: var(--orange);
    background-image:
      linear-gradient(to right, var(--yellow) 2px, transparent 2px),
      linear-gradient(to bottom, var(--yellow) 2px, transparent 2px);
    background-size: 60px 33.75px;
    background-position: -1px -1px;
    font-family: "Archivo", "Helvetica Neue", Arial, sans-serif;
  }
  .title-card-shadow {
    position: absolute;
    left: 276px;
    top: 157px;
    width: 660px;
    height: 372px;
    background: var(--yellow);
  }
  .title-card {
    position: absolute;
    left: 262px;
    top: 188px;
    width: 660px;
    height: 328px;
    box-sizing: border-box;
    background: var(--orange);
    border: 5px solid var(--yellow);
    display: flex;
    align-items: center;
    justify-content: center;
  }
  .title {
    margin: 0;
    color: var(--yellow);
    font-weight: 800;
    font-size: 52px;
    line-height: 1.22;
    letter-spacing: 0.14em;
    text-align: center;
    padding-left: 0.14em;
  }
  .category-tag {
    position: absolute;
    left: 156px;
    top: 121px;
    width: 294px;
    height: 54px;
    box-sizing: border-box;
    background: var(--teal);
    border: 3px solid var(--navy);
    box-shadow: 7px 7px 0 var(--navy);
    color: var(--yellow);
    font-weight: 800;
    font-size: 30px;
    display: flex;
    align-items: center;
    justify-content: center;
    letter-spacing: 0.01em;
  }
  .category-tag sup {
    font-size: 0.55em;
    margin-right: 6px;
    position: relative;
    top: -0.2em;
  }
</style>
</head>
<body>
  <main class="slide">
    <div class="title-card-shadow"></div>
    <section class="title-card">
      <h1 class="title">GENERAL<br>KNOWLEDGE</h1>
    </section>
    <div class="category-tag">1<sup>st</sup>CATEGORY</div>
  </main>
</body>
</html>
```